High end business card design for custom homebuilding company

Looking for a high end business card design that is unique and elegant. Can use embossing, foil printing, laser die cutting, or any high end printing technique or high end paper. Will upload current design so you can see the logo and what we are using currently, but we want something more unique and elegant. I included our logo to help with design.

Target Market(s)

High end custom home buyers of $1.5 million plus homes. Also real estate developers of high end communities.

Industry/Entity Type

Business

Contact Information for Business Card

Double sided. We want something very elegant and expensive looking. We are looking to incorporate a combination of perhaps linen paper or a high end paper, with foil stamping or embossing/debossing to make the card look unique, but still elegant. We tend to use blacks and golds, but are open to any ideas. Looking for creative and unique design.

Colors

Designer to choose colors to be used in the design.

Requirements
Must have
• High end, elegant look. Can use foil, embossing, or high end papers like linen. We want to make the card unique and interesting, but elegant and expensive looking.
Nice to have
• I am including just some cards I saw that looked interesting for one reason or another. I like a clean elegant design and like both the clean white style, and the blacks. So not sure if we want a black design or white. Would like to see both.

```html
<!DOCTYPE html>
<html lang="en">
<head>
<meta charset="utf-8">
<title>Ridgeline Custom Homes – Business Card</title>
<link rel="stylesheet" href="https://fonts.googleapis.com/css2?family=Cinzel:wght@400&family=Arvo:wght@700&family=Montserrat:wght@500&display=swap">
<style>
  :root {
    --backdrop: #a9dde0;
    --card: #2a2a2b;
    --copper-deep: #a9581f;
    --copper: #c07a3e;
    --copper-light: #ecc8aa;
    --foil: #d7a47a;
    --foil-text: #cf935e;
    --name: #b8834d;
  }
  * { margin: 0; padding: 0; box-sizing: border-box; }
  html, body { width: 1200px; height: 1200px; overflow: hidden; }
  body { background: var(--backdrop); position: relative; }

  .card {
    position: absolute;
    left: 150px;
    width: 900px;
    height: 522px;
    background: var(--card);
    overflow: hidden;
  }
  .card--front { top: 40px; }
  .card--back { top: 640px; }

  .card__shapes { position: absolute; inset: 0; width: 100%; height: 100%; }

  .brand {
    position: absolute;
    color: var(--foil);
    font-family: "Cinzel", serif;
    font-weight: 400;
    white-space: nowrap;
  }
  .brand__mark {
    position: absolute;
    border: 3px solid var(--foil);
    border-radius: 50%;
  }
  .brand__name { display: block; line-height: 1; letter-spacing: 1px; }
  .brand__tagline { display: block; line-height: 1; letter-spacing: 0.62em; }

  .card--front .brand { left: 292px; top: 188px; }
  .card--front .brand__mark { left: -126px; top: 2px; width: 96px; height: 96px; }
  .card--front .brand__name { font-size: 82px; }
  .card--front .brand__tagline { font-size: 24px; margin-top: 2px; }

  .card--back .brand { left: 292px; top: 100px; }
  .card--back .brand__mark { left: -96px; top: 4px; width: 76px; height: 76px; }
  .card--back .brand__name { font-size: 64px; }
  .card--back .brand__tagline { font-size: 19px; margin-top: 2px; }

  .contact {
    position: absolute;
    left: 86px;
    top: 340px;
    font-family: "Montserrat", sans-serif;
    font-weight: 500;
    font-size: 22px;
    line-height: 29px;
    color: var(--foil-text);
  }
  .contact__web { margin-top: 29px; }

  .person {
    position: absolute;
    left: 489px;
    top: 345px;
  }
  .person__name {
    font-family: "Arvo", serif;
    font-weight: 700;
    font-size: 37px;
    line-height: 1.1;
    color: var(--name);
  }
  .person__title {
    font-family: "Montserrat", sans-serif;
    font-weight: 500;
    font-size: 20px;
    margin-top: 4px;
    color: var(--name);
  }
  .person__rule {
    width: 80px;
    height: 3px;
    background: var(--name);
    margin-top: 32px;
  }
</style>
</head>
<body>
  <svg width="0" height="0" style="position:absolute">
    <defs>
      <linearGradient id="copperSheen" x1="0" y1="1" x2="1" y2="0">
        <stop offset="0" stop-color="var(--copper-deep)"/>
        <stop offset="0.55" stop-color="var(--copper)"/>
        <stop offset="1" stop-color="var(--copper-light)"/>
      </linearGradient>
      <linearGradient id="copperCorner" x1="0" y1="0" x2="1" y2="1">
        <stop offset="0" stop-color="#c2874f"/>
        <stop offset="1" stop-color="var(--copper-deep)"/>
      </linearGradient>
    </defs>
  </svg>

  <section class="card card--front">
    <svg class="card__shapes" viewBox="0 0 1121 652" preserveAspectRatio="none" aria-hidden="true">
      <polygon points="0,0 431,0 137,168 78,482 0,397" fill="url(#copperSheen)"/>
      <polygon points="590,490 903,557 1121,357 1121,652 665,652" fill="url(#copperCorner)"/>
    </svg>
    <div class="brand">
      <span class="brand__mark"></span>
      <span class="brand__name">RIDGELINE</span>
      <span class="brand__tagline">CUSTOM HOMES</span>
    </div>
  </section>

  <section class="card card--back">
    <svg class="card__shapes" viewBox="0 0 1121 652" preserveAspectRatio="none" aria-hidden="true">
      <polygon points="0,0 432,0 137,170 77,482 0,395" fill="url(#copperSheen)"/>
    </svg>
    <div class="brand">
      <span class="brand__mark"></span>
      <span class="brand__name">RIDGELINE</span>
      <span class="brand__tagline">CUSTOM HOMES</span>
    </div>
    <div class="contact">
      <p class="contact__email">elias@ridgelinehomes.com</p>
      <p class="contact__phone">+91 555-010-2468</p>
      <p class="contact__web">www.ridgelinehomes.com</p>
    </div>
    <div class="person">
      <p class="person__name">Elias Varden</p>
      <p class="person__title">Co-Founder &amp; CEO</p>
      <div class="person__rule"></div>
    </div>
  </section>
</body>
</html>
```